Brightwell Feline Clinic Business Card Design

I need a business card designed for my cat only veterinary clinic. I will upload the logo that I would like included on the card. Please include:
Business Name: Brightwell Feline Clinic
Address: 4827 W. 39th Ln, Scottsdale, AZ 85317
Phone #: 480-555-6314
Website URL: www.brightwellfeline.example
And the Doctors Name: Marla Quint, DVM

```html
<!DOCTYPE html>
<html lang="en">
<head>
<meta charset="utf-8">
<title>Brightwell Feline Clinic – Business Card</title>
<link rel="stylesheet" href="https://fonts.googleapis.com/css2?family=Montserrat:wght@400;500;700&display=swap">
<style>
  :root {
    --page-bg: #ece8e1;
    --card-bg: #f9f9f9;
    --card-back-bg: #ffffff;
    --ink: #111111;
    --text: #222222;
    --green: #3d7f2b;
    --green-band: #356f26;
    --mark-dark: #1c1830;
    --mark-mid: #3a2f5c;
  }
  * { margin: 0; padding: 0; box-sizing: border-box; }
  html, body { width: 900px; height: 1200px; overflow: hidden; }
  body {
    position: relative;
    background: var(--page-bg);
    font-family: "Montserrat", Arial, sans-serif;
    color: var(--text);
  }
  .card {
    position: absolute;
    left: 80px;
    width: 742px;
    height: 440px;
    border-radius: 28px;
    overflow: hidden;
    box-shadow: 0 4px 10px rgba(0,0,0,0.25);
  }
  .card--front { top: 132px; background: var(--card-bg); }
  .card--back { top: 638px; background: var(--card-back-bg); }
  .card__band {
    position: absolute;
    left: 0; right: 0; bottom: 0;
    height: 13px;
    background: var(--green-band);
  }
  .brand { position: absolute; display: flex; align-items: center; }
  .brand__mark {
    border-radius: 50%;
    background: radial-gradient(circle at 50% 40%, var(--mark-mid), var(--mark-dark) 70%);
    flex: none;
  }
  .brand__name {
    font-family: "Montserrat", Arial, sans-serif;
    font-weight: 500;
    color: var(--ink);
    white-space: nowrap;
  }
  .card--front .brand { left: 45px; top: 52px; }
  .card--front .brand__mark { width: 148px; height: 148px; margin-right: 14px; }
  .card--front .brand__name { font-size: 31px; line-height: 37px; }
  .card--back .brand { left: 114px; top: 124px; }
  .card--back .brand__mark { width: 192px; height: 192px; margin-right: 16px; }
  .card--back .brand__name { font-size: 40px; line-height: 47px; }

  .doctor {
    position: absolute;
    left: 33px; top: 303px;
    font-weight: 700;
    font-size: 27px;
    color: var(--green);
  }
  .divider {
    position: absolute;
    left: 33px; top: 350px;
    width: 671px; height: 1.5px;
    background: var(--green);
  }
  .contact {
    position: absolute;
    left: 35px; top: 362px;
    list-style: none;
    font-size: 16px;
    line-height: 22px;
  }
  .contact li { display: flex; align-items: center; }
  .contact svg { width: 14px; height: 14px; margin-right: 14px; fill: var(--green); }
  .address {
    position: absolute;
    left: 493px; top: 368px;
    font-size: 16px;
    line-height: 21px;
    font-style: normal;
  }
</style>
</head>
<body>
  <section class="card card--front">
    <div class="brand">
      <div class="brand__mark" role="img" aria-label="Clinic emblem"></div>
      <div class="brand__name">Brightwell<br>Feline Clinic</div>
    </div>
    <h1 class="doctor">Marla Quint, DVM</h1>
    <div class="divider"></div>
    <ul class="contact">
      <li>
        <svg viewBox="0 0 16 16" aria-hidden="true"><path d="M1 6c0-2 3-3 7-3s7 1 7 3v1h-3V5.5H4V7H1zM3 8h10l1 6H2z"/></svg>
        480-555-6314
      </li>
      <li>
        <svg viewBox="0 0 16 16" aria-hidden="true"><circle cx="8" cy="8" r="7"/></svg>
        www.brightwellfeline.example
      </li>
    </ul>
    <address class="address">4827 W. 39th Ln, Scottsdale<br>AZ 85317</address>
    <div class="card__band"></div>
  </section>

  <section class="card card--back">
    <div class="brand">
      <div class="brand__mark" role="img" aria-label="Clinic emblem"></div>
      <div class="brand__name">Brightwell<br>Feline Clinic</div>
    </div>
    <div class="card__band"></div>
  </section>
</body>
</html>
```